New cosmetics company needs packaging design

We need a packaging design for our new cosmetics brand. We are looking for modern, sleek packaging such as black or white packaging with gold text. The packaging will be for boxes of different sizes for eye pencils, lipsticks, foundation etc. For example small long rectangle boxes, standing rectangle boxes and square boxes for products.
Attached is a pattern we were thinking to be used on the inside of the boxes and maybe some elements of this pattern on the outside of the boxes. This is not a strict requirement, we are happy to receive other ideas.
Our logo is a 5-letter word and we have a round symbol, which we'll be happy to send after seeing some designs.
Thank you.

```html
<!DOCTYPE html>
<html lang="en">
<head>
<meta charset="utf-8">
<title>LUNEA eye pencil box – flat panels</title>
<link href="https://fonts.googleapis.com/css2?family=Josefin+Sans:wght@300;400;600&family=Nunito:wght@700;800&display=swap" rel="stylesheet">
<style>
  :root{
    --canvas:#ffffff;
    --floor:#f7f7f7;
    --teal:#2fc4b0;
    --teal-deep:#1f8c7a;
    --teal-block:#23a08f;
    --gold:#b8862b;
    --gold-light:#d9ad4f;
    --pink:#ec3f8f;
    --orange:#f4a13c;
    --grey:#8c8c8c;
    --ink:#111111;
    --white:#ffffff;
    --edge:#c79a52;
  }
  *{box-sizing:border-box;margin:0;padding:0}
  html,body{width:1200px;height:708px;overflow:hidden}
  body{
    background:linear-gradient(180deg,var(--canvas) 0%,var(--canvas) 78%,var(--floor) 100%);
    font-family:"Josefin Sans",sans-serif;
    position:relative;
  }
  .panel{position:absolute;top:47px;width:93px;height:566px;border:1px solid var(--edge);overflow:hidden}
  .panel-back{left:128px;background:var(--teal)}
  .panel-side{left:282px;background:var(--white)}
  .panel-front{left:426px;background:var(--white);border-right-color:#e8d84a}
  .panel-top{position:absolute;left:556px;top:107px;width:93px;height:93px;border:1px solid #e3c9a0;background:var(--white)}

  .pattern{position:absolute;left:0;width:100%}
  .back-wash{top:0;height:100%;background:radial-gradient(circle at 30% 30%,rgba(255,255,255,.18),transparent 60%),radial-gradient(circle at 70% 60%,rgba(255,255,255,.12),transparent 55%)}
  .back-floral{bottom:0;height:75px;background:linear-gradient(180deg,rgba(255,255,255,0),rgba(255,255,255,.35))}
  .side-floral-top{top:0;height:280px;background:linear-gradient(160deg,#e8f5f1 0%,#7bbfa9 40%,#f5c1d6 70%,#e7f3ef 100%)}
  .side-floral-bottom{top:305px;height:261px;background:linear-gradient(200deg,#f6f0ea 0%,#f7c68c 30%,#8fcab8 60%,#f3d6e5 85%,#eef6f3 100%)}
  .front-floral{top:276px;height:290px;background:linear-gradient(180deg,#ffffff 0%,#cfe9df 35%,#a9d8c6 100%)}

  .mark{display:flex;flex-direction:column;align-items:center;gap:6px}
  .mark-dot{width:40px;height:40px;border-radius:50%}
  .mark-name{font-weight:300;letter-spacing:2px;font-size:14px}

  .back-mark{position:absolute;top:28px;left:0;width:100%}
  .back-mark .mark-dot{background:rgba(31,140,122,.55)}
  .back-mark .mark-name{color:rgba(31,140,122,.9)}
  .back-dots{position:absolute;top:132px;left:0;width:100%;text-align:center;color:var(--teal-deep);font-size:10px;letter-spacing:4px}

  .rule{position:absolute;height:1px}
  .back-rule{left:22px;width:50px;background:rgba(255,255,255,.85)}
  .back-title{position:absolute;top:196px;left:0;width:100%;text-align:center;font-weight:600;font-size:11px;letter-spacing:1px;color:var(--gold-light)}
  .back-copy{position:absolute;top:218px;left:4px;right:4px;text-align:center;color:var(--white);font-size:8.6px;line-height:11.4px}
  .back-copy p+p{margin-top:0}

  .side-band{position:absolute;top:280px;left:0;width:100%;height:25px;background:var(--white);text-align:center;font-weight:300;font-size:18px;letter-spacing:2px;color:var(--teal-deep);line-height:29px}

  .front-block{position:absolute;top:1px;left:12px;width:70px;height:131px;background:var(--teal-block);padding-top:22px}
  .front-block .mark-dot{width:44px;height:44px;border:2px solid var(--white)}
  .front-block .mark-name{color:var(--white);font-size:15px;margin-top:12px}
  .shade-swatch{position:absolute;top:160px;left:35px;width:28px;height:14px;border-radius:7px;background:linear-gradient(90deg,#6d6d6d,#9a9a9a)}
  .front-rule{left:20px;width:53px;background:var(--gold-light)}
  .front-title{position:absolute;top:228px;left:0;width:100%;text-align:center;font-weight:600;font-size:10.5px;letter-spacing:1px;color:var(--gold)}
  .front-copy{position:absolute;top:246px;left:0;width:100%;text-align:center;font-size:8.6px;line-height:11px;color:var(--gold-light)}

  .top-mark{position:absolute;top:14px;left:0;width:100%}
  .top-mark .mark-dot{width:44px;height:44px;background:var(--grey)}
  .top-mark .mark-name{color:var(--grey);font-size:11px}

  .note{position:absolute;font-family:"Nunito",sans-serif;font-weight:800;color:var(--ink);font-size:11px}
  .note-pencil{left:556px;top:80px}
  .arrow{position:absolute}
  .label{position:absolute;top:629px;font-family:"Nunito",sans-serif;font-weight:800;font-size:11px;color:var(--ink);text-align:center;width:120px}
</style>
</head>
<body>

  <section class="panel panel-back" aria-label="Back panel">
    <div class="pattern back-wash" role="img" aria-label="Soft pale floral pattern over teal"></div>
    <div class="back-mark mark"><span class="mark-dot"></span><span class="mark-name">LUNEA</span></div>
    <div class="back-dots">•••</div>
    <div class="rule back-rule" style="top:162px"></div>
    <h2 class="back-title">PERFECT</h2>
    <div class="back-copy">
      <p>nisi elit consequa ipsum, nec sag sum, nec sagitt</p>
      <p>nisi elit consequa ipsum, nec sag sumtt</p>
      <p>nisi elit consequa ipsum, nec sag sumtt</p>
      <p>nisi sequa ipsum, nec sag sum, nec sagitt</p>
      <p>nisi elit consequa ipsum, nec sag sumtt</p>
      <p>nisi elit consequa ipsum, nec sag sum, nec sagitt</p>
      <p>nisi elit consequa ipsum, nec sag sum, nec sagitt</p>
    </div>
    <div class="rule back-rule" style="top:469px"></div>
    <div class="pattern back-floral" role="img" aria-label="White line-drawn flowers and leaves"></div>
  </section>

  <section class="panel panel-side" aria-label="Side panel">
    <div class="pattern side-floral-top" role="img" aria-label="Teal leaves, pink swirls and tulips floral pattern"></div>
    <div class="side-band">LUNEA</div>
    <div class="pattern side-floral-bottom" role="img" aria-label="Orange, pink and teal flowers with vines"></div>
  </section>

  <section class="panel panel-front" aria-label="Front panel">
    <div class="front-block mark"><span class="mark-dot"></span><span class="mark-name">LUNEA</span></div>
    <div class="shade-swatch" role="img" aria-label="Grey pencil stroke showing the shade"></div>
    <svg class="arrow" style="left:83px;top:170px" width="30" height="20" viewBox="0 0 30 20" aria-hidden="true">
      <path d="M28 2 C24 12 14 16 4 14" fill="none" stroke="#111" stroke-width="1.6"/>
      <path d="M9 9 L3 14 L10 17" fill="none" stroke="#111" stroke-width="1.6"/>
    </svg>
    <div class="rule front-rule" style="top:214px"></div>
    <h2 class="front-title">CONSEMI</h2>
    <p class="front-copy">nisi elit consequa<br>ipsum, nec sag</p>
    <div class="rule front-rule" style="top:267px"></div>
    <div class="pattern front-floral" role="img" aria-label="Teal outline flowers and vines"></div>
  </section>

  <p class="note note-pencil">color of eye pencil</p>
  <svg class="arrow" style="left:556px;top:92px" width="30" height="30" viewBox="0 0 30 30" aria-hidden="true">
    <path d="M4 2 C0 14 10 22 24 24" fill="none" stroke="#111" stroke-width="1.6"/>
    <path d="M18 18 L25 24 L17 28" fill="none" stroke="#111" stroke-width="1.6"/>
  </svg>
  <section class="panel-top" aria-label="Top panel">
    <div class="top-mark mark"><span class="mark-dot"></span><span class="mark-name">LUNEA</span></div>
  </section>
  <p class="label" style="left:543px;top:215px;width:120px">Top</p>

  <p class="label" style="left:114px">Back</p>
  <p class="label" style="left:268px">Left side or right</p>
  <p class="label" style="left:405px">Front</p>

</body>
</html>
```